Pelin Thai Massage Double Sided Flyer Luxury

I require a double sided flyer
we are a Thai Massage Spa
Would like gold, deep purple and bronze colours
Something eye catching and looks professional

```html
<!DOCTYPE html>
<html lang="en">
<head>
<meta charset="utf-8">
<title>Pelin Thai Massage – Double Sided Flyer</title>
<link rel="stylesheet" href="https://fonts.googleapis.com/css2?family=Marcellus&family=Lato:wght@400;700&display=swap">
<style>
  :root {
    --plum-stage: #1e0a2b;
    --purple: #3b1650;
    --gold: #fcc74d;
    --gold-text: #f2b938;
    --bronze: #d3822f;
    --bronze-text: #c9782a;
    --white: #ffffff;
    --skin-light: #d9a57a;
    --skin-dark: #7b4a2c;
  }
  * { margin: 0; padding: 0; box-sizing: border-box; }
  html, body { width: 1200px; height: 1200px; overflow: hidden; }
  body { background: var(--plum-stage); position: relative; font-family: "Lato", sans-serif; }

  .flyer-slot { position: absolute; top: 220px; width: 539px; height: 760px; overflow: hidden; }
  .flyer-slot--front { left: 46px; }
  .flyer-slot--back { left: 613px; }

  .flyer { position: absolute; left: 0; top: 0; width: 673px; height: 950px; background: var(--white);
           transform: scale(0.8); transform-origin: 0 0; color: var(--purple); }
  .flyer__art { position: absolute; inset: 0; width: 673px; height: 950px; }
  .abs { position: absolute; }

  .heading { font-family: "Marcellus", serif; color: var(--purple); }
  .heading--page { left: 43px; top: 34px; font-size: 41px; letter-spacing: 0.5px; }
  .intro { left: 43px; top: 90px; width: 258px; font-size: 18.5px; line-height: 25px; }

  .treatment-title { left: 278px; font-size: 26px; line-height: 34px; width: 370px; }
  .duration { left: 278px; font-size: 19px; color: var(--bronze-text); }
  .detail { left: 278px; font-size: 14.5px; line-height: 19.5px; width: 190px; }
  .price { right: 75px; font-family: "Marcellus", serif; font-size: 36px; color: var(--bronze-text); }
  .divider { left: 278px; top: 469px; width: 319px; height: 1.5px; background: var(--purple); }

  .contact { left: 188px; color: var(--white); font-size: 19px; line-height: 22px; }
  .contact-icon { left: 161px; width: 20px; height: 20px; }
  .brand-mark { left: 52px; top: 800px; width: 62px; height: 62px; border: 2px solid var(--white); border-radius: 50%; }
  .brand-name { left: 20px; top: 865px; width: 130px; text-align: center; color: var(--white); font-size: 14px; }
  .vouchers { left: 395px; top: 811px; font-family: "Marcellus", serif; font-size: 20px; color: var(--gold-text); }
  .open-days { left: 376px; top: 842px; font-family: "Marcellus", serif; font-size: 29px; color: var(--white); }
  .website { left: 0; top: 897px; width: 673px; text-align: center; color: var(--white); font-size: 19px; letter-spacing: 5px; }

  .back-mark { left: 280px; top: 40px; width: 112px; height: 112px; border: 3px solid var(--gold); border-radius: 50%; }
  .back-brand { left: 0; top: 156px; width: 673px; text-align: center; font-size: 27px; color: var(--gold-text); }
  .welcome { left: 43px; top: 590px; font-family: "Marcellus", serif; color: var(--white); font-size: 33px; line-height: 1; }
  .luxury { left: 43px; top: 622px; font-family: "Marcellus", serif; color: var(--white); font-size: 58px; line-height: 1; }
  .about { left: 45px; width: 585px; font-size: 17.5px; line-height: 23px; }
</style>
</head>
<body>

  <!-- Front side: treatments and prices -->
  <section class="flyer-slot flyer-slot--front">
    <div class="flyer">
      <svg class="flyer__art" viewBox="0 0 673 950" xmlns="http://www.w3.org/2000/svg">
        <defs>
          <linearGradient id="skin-a" x1="0" y1="0" x2="1" y2="1">
            <stop offset="0" stop-color="var(--skin-light)"/>
            <stop offset="1" stop-color="var(--skin-dark)"/>
          </linearGradient>
          <linearGradient id="skin-b" x1="0" y1="0" x2="1" y2="1">
            <stop offset="0" stop-color="#f0cfc4"/>
            <stop offset="1" stop-color="#9c6a55"/>
          </linearGradient>
        </defs>
        <path d="M0 0H673V240C480 230 300 290 0 272Z" fill="var(--gold)"/>
        <path role="img" aria-label="Photo: woman smiling while receiving a shoulder massage"
              d="M495 0H673V238C560 226 460 240 345 270C325 200 345 90 495 0Z" fill="url(#skin-a)"/>
        <path d="M0 298C200 310 380 245 673 205V250C450 262 250 330 0 330Z" fill="var(--purple)"/>
        <path d="M290 282C420 228 560 222 673 238V365C620 300 500 272 290 282Z" fill="var(--bronze)"/>
        <path d="M0 545C80 720 300 800 673 790V893H0Z" fill="var(--purple)"/>
        <rect y="893" width="673" height="37" fill="var(--bronze)"/>
        <rect y="930" width="673" height="20" fill="var(--gold)"/>
        <circle cx="143" cy="456" r="88" fill="var(--gold)"/>
        <circle role="img" aria-label="Photo: deep tissue back massage" cx="143" cy="456" r="70" fill="url(#skin-a)"/>
        <circle cx="148" cy="674" r="88" fill="var(--gold)"/>
        <circle role="img" aria-label="Photo: woman receiving a traditional Thai head massage" cx="148" cy="674" r="70" fill="url(#skin-b)"/>
      </svg>

      <h1 class="abs heading heading--page">MASSAGES</h1>
      <p class="abs intro">Restore balance. Revive your senses. Discover all the ways Pelin Thai Massage can breathe new life into your body and soul.</p>

      <h2 class="abs heading treatment-title" style="top:338px">DEEP TISSUE MASSAGE</h2>
      <p class="abs duration" style="top:386px">60 minutes</p>
      <p class="abs detail" style="top:414px">Oil massage personalised, light to firm pressure</p>
      <p class="abs price" style="top:402px">£45</p>
      <div class="abs divider"></div>
      <p class="abs duration" style="top:477px">90 minutes</p>
      <p class="abs detail" style="top:504px">Oil massage, medium to firm pressure</p>
      <p class="abs price" style="top:494px">£55</p>

      <h2 class="abs heading treatment-title" style="top:588px">THAI FLOOR TRADTIONAL MASSAGE</h2>
      <p class="abs duration" style="top:666px">60 minutes</p>
      <p class="abs detail" style="top:694px">Dry massage, medium to firm pressure applying stretching technique</p>
      <p class="abs price" style="top:692px">£45</p>

      <div class="abs brand-mark"></div>
      <p class="abs brand-name">Pelin Thai Massage</p>

      <svg class="abs contact-icon" style="top:804px" viewBox="0 0 20 20" aria-hidden="true">
        <rect width="20" height="20" rx="3" fill="var(--white)"/>
        <path d="M6 4.5c-1 .6-1.6 1.7-1 3.3 1.2 3.3 3.9 6 7.2 7.2 1.6.6 2.7 0 3.3-1l-2.4-2.1-1.5 1c-1.6-.8-2.9-2.1-3.7-3.7l1-1.5Z" fill="var(--purple)"/>
      </svg>
      <p class="abs contact" style="top:802px">0100 555 0142</p>
      <svg class="abs contact-icon" style="top:835px" viewBox="0 0 20 20" aria-hidden="true">
        <path d="M10 1a6.5 6.5 0 0 0-6.5 6.5C3.5 12 10 19 10 19s6.5-7 6.5-11.5A6.5 6.5 0 0 0 10 1Zm0 9a2.5 2.5 0 1 1 0-5 2.5 2.5 0 0 1 0 5Z" fill="var(--white)"/>
      </svg>
      <p class="abs contact" style="top:833px">42 Willow Row<br>Hartfield HF3 2QN</p>

      <p class="abs vouchers">Gift Vouchers Available</p>
      <p class="abs open-days">Open 7 Days a Week</p>
      <p class="abs website">www.pelinthaimassage.co.uk</p>
    </div>
  </section>

  <!-- Back side: welcome -->
  <section class="flyer-slot flyer-slot--back">
    <div class="flyer">
      <svg class="flyer__art" viewBox="0 0 673 950" xmlns="http://www.w3.org/2000/svg">
        <defs>
          <linearGradient id="skin-c" x1="0" y1="0" x2="1" y2="1">
            <stop offset="0" stop-color="#e2b48e"/>
            <stop offset="0.6" stop-color="#b07850"/>
            <stop offset="1" stop-color="#5a3420"/>
          </linearGradient>
        </defs>
        <path d="M0 0H300C220 55 110 78 0 80Z" fill="var(--bronze)"/>
        <path d="M0 165C200 235 430 180 673 198V260C430 225 200 270 0 250Z" fill="var(--gold)"/>
        <path role="img" aria-label="Photo: woman relaxing during a back massage at a candlelit spa"
              d="M0 222C200 248 420 190 673 226V412C420 432 220 560 0 562Z" fill="url(#skin-c)"/>
        <path d="M0 560C220 560 420 432 673 405V430C500 460 420 712 260 712H0Z" fill="var(--purple)"/>
        <path d="M300 950C450 930 560 900 673 880V950Z" fill="var(--bronze)"/>
        <path d="M0 950H320C200 945 80 945 0 940Z" fill="var(--bronze)"/>
      </svg>

      <div class="abs back-mark"></div>
      <p class="abs back-brand">Pelin Thai Massage</p>

      <p class="abs welcome">Welcome to</p>
      <p class="abs luxury">Luxury</p>

      <p class="abs about" style="top:730px">Set in the heart of Oakmere, Pelin Thai Massage will allow you to immerse yourself in a place where your wellbeing and rejuvenation is at the centre of what we do.</p>
      <p class="abs about" style="top:822px">Using Thai traditions, our highly trained therapists offer revitalising body treatments with their deep tissue massage techniques. In their hands, you will see and feel immediate results.</p>
    </div>
  </section>

</body>
</html>
```